Flyer-Design für Startup
Zielgruppe
Unser Unternehmen ist ein Startup in der Bildungslandschaft. Hinsichtlich dem Flyer besteht die Zielgruppe aus Studierenden im Alter zwischen 25 und 40 Jahren.
Aufgabenstellung
Die Texte sollten in der Vektor Datei bearbeitbare sein!
Die Frau im Feld sowie die Farben des Logos sollten im Flyer berücksichtigt werden. Zudem sollen die Inhalte auch grafisch aufgearbeitet werden. Format: Es soll ein 6-seitiger Zickzackfalz sein.
Unsere Webseite ist vorübergehend nur im Entwurfsmodus durch das Passwort 'torvilak4726' erreichbar.
Schriftart Helvetica!

```html
<!DOCTYPE html>
<html lang="de">
<head>
<meta charset="utf-8">
<title>Lernhöhe – Aufstiegsfortbildung Flyer</title>
<link rel="stylesheet" href="https://fonts.googleapis.com/css2?family=Bodoni+Moda:wght@600;700&family=Jost:wght@400;500;600&display=swap">
<style>
:root{
  --navy:#1f2b4f;
  --navy-soft:#2c3a63;
  --paper:#e7e7ea;
  --paper-white:#f3f3f5;
  --ink-grey:#6d6e76;
  --white:#ffffff;
  --stage:#e9e9eb;
  --sky-top:#ece5d2;
  --sky-mid:#b9c6cb;
  --field:#b7894f;
}
*{box-sizing:border-box;margin:0;padding:0}
html,body{width:667px;height:1200px;overflow:hidden;background:var(--stage)}
body{position:relative;font-family:"Jost",Helvetica,Arial,sans-serif;color:var(--ink-grey)}
.sheet{position:absolute;left:20px;width:627px;height:443px;display:flex;box-shadow:0 6px 18px rgba(0,0,0,.18)}
.sheet--outside{top:150px}
.sheet--inside{top:627px}
.panel{position:relative;width:209px;height:443px;overflow:hidden}
.panel section{position:relative}
.panel--light{background:var(--paper)}
.panel--navy{background:linear-gradient(90deg,var(--navy) 0%,var(--navy-soft) 100%);color:var(--white)}
.heading{font-family:"Bodoni Moda",Georgia,serif;font-weight:700;letter-spacing:.12em;text-transform:uppercase;font-size:8.4px;line-height:1.1;margin-bottom:3px}
.panel--light .heading{color:var(--navy)}
.body-text{font-size:6.1px;line-height:1.38;letter-spacing:.03em}
.body-text b{font-weight:600}
.subhead{font-size:6.1px;font-weight:600;margin-top:2px}
.list{list-style:none;font-size:6.1px;line-height:1.38;letter-spacing:.03em}
.list li{padding-left:6px;position:relative}
.list li::before{content:"•";position:absolute;left:0}
.vertical-title{position:absolute;writing-mode:vertical-rl;font-family:"Bodoni Moda",Georgia,serif;font-weight:700;font-size:27px;line-height:1}
.brand-tab{position:absolute;top:0;background:var(--navy);display:flex;align-items:center;justify-content:center;gap:4px;clip-path:polygon(0 0,100% 0,100% 100%,50% 78%,0 100%)}
.brand-name{font-family:"Jost",Helvetica,sans-serif;font-weight:500;color:var(--white);font-size:11px;letter-spacing:.02em}
.brand-dot{width:5px;height:5px;background:var(--white)}
.brand-line{display:flex;align-items:center;gap:4px}
.icon{position:absolute}
.footer-bar{position:absolute;bottom:0;height:14px;background:var(--navy)}

/* Outside: Zielsetzung */
.goal .brand-tab{left:36px;width:112px;height:46px}
.goal .content{position:absolute;left:14px;top:70px;width:145px}
.goal .vertical-title{right:14px;top:58px;color:var(--navy)}
.goal .footer-bar{left:50px;width:100px}
.goal .schedule-line{width:112px;margin-top:3px}

/* Outside: Kosten / Inhalte */
.facts .content{position:absolute;left:14px;top:14px;width:184px}
.facts section{margin-bottom:9px}

/* Cover */
.cover-photo{position:absolute;inset:0;background:linear-gradient(180deg,var(--sky-top) 0%,var(--sky-mid) 45%,#c7b28b 62%,var(--field) 100%)}
.cover .brand-tab{left:58px;width:94px;height:40px}
.cover-title{position:absolute;top:50px;left:0;width:100%;text-align:center;color:var(--navy)}
.cover-title .brand-name{color:var(--navy);font-size:15px;font-weight:500}
.cover-title h1{font-family:"Bodoni Moda",Georgia,serif;font-weight:700;font-size:14px;letter-spacing:.04em;margin-top:2px}
.cover-band{position:absolute;bottom:0;left:0;width:100%;height:82px;background:var(--navy);color:var(--white);text-align:center;font-family:"Bodoni Moda",Georgia,serif;font-size:12.5px;line-height:1.3;padding-top:20px;letter-spacing:.03em}
.cover-band b{font-weight:700}

/* Inside: Aufstiegsfortbildung */
.career .content{position:absolute;left:14px;top:64px;width:135px}
.career .content p{margin-bottom:7px}
.career .vertical-title{right:12px;top:40px;color:var(--white)}
.career .brand-line{position:absolute;left:34px;top:22px}
.career .brand-name{font-size:10px}

/* Inside: Fachliche Voraussetzungen */
.entry .brand-tab{left:56px;width:98px;height:40px}
.entry .content{position:absolute;left:12px;top:52px;width:186px}
.entry .list{font-size:5.6px}
.entry .body-text{font-size:5.6px}
.entry .note{font-size:4.8px;line-height:1.35;margin-top:4px}
.entry .footer-bar{left:60px;width:90px}

/* Inside: Technische Voraussetzungen */
.tech .vertical-title{left:10px;top:30px;color:var(--white)}
.tech .brand-line{position:absolute;left:70px;top:22px}
.tech .brand-name{font-size:10px}
.tech .content{position:absolute;left:48px;top:48px;width:150px}
.tech .list{font-size:5.2px;line-height:1.4}
.tech section{margin-bottom:10px}
.contact{position:absolute;right:14px;bottom:16px;text-align:right;font-size:7px;line-height:1.4;letter-spacing:.03em}
.contact p+p{margin-top:6px}
</style>
</head>
<body>

<div class="sheet sheet--outside">

  <div class="panel panel--light goal">
    <div class="brand-tab"><span class="brand-dot"></span><span class="brand-name">Lernhöhe</span></div>
    <div class="content">
      <section>
        <h2 class="heading">Zielsetzung</h2>
        <svg class="icon" style="left:0;top:14px" width="30" height="30" viewBox="0 0 30 30" fill="none" stroke="#9a9aa0" stroke-width="1.6">
          <path d="M15 3c-5 0-8 3.5-8 8 0 6 8 13 8 13s8-7 8-13c0-4.5-3-8-8-8z"/><circle cx="15" cy="11" r="3"/><ellipse cx="15" cy="25" rx="11" ry="3"/>
        </svg>
        <p class="body-text" style="margin-left:34px">Dieser Kurs bereitet Sie auf die Prüfung zum/r geprüften Wirtschaftsfachwirt/in (IHK) vor.</p>
        <p class="body-text" style="margin-top:8px">Die Anmeldung zur Prüfung bei der für Sie örtlich zuständigen Industrie- und Handelskammer erfolgt durch den Teilnehmer und die Prüfung ist innerhalb des Maßnahmenzeitraums abzulegen.</p>
      </section>
      <section style="margin-top:12px">
        <h2 class="heading">Vollzeit</h2>
        <svg class="icon" style="left:118px;top:10px" width="28" height="27" viewBox="0 0 34 32" fill="none" stroke="#9a9aa0" stroke-width="1.6">
          <rect x="2" y="5" width="24" height="21" rx="2"/><path d="M2 11h24M8 2v6M20 2v6"/><path d="M7 15h3M12 15h3M17 15h3M7 20h3M12 20h3"/><circle cx="25" cy="23" r="7" fill="#e7e7ea"/><path d="M25 19v4l3 2"/>
        </svg>
        <p class="body-text" style="width:112px"><b>Kursformat :</b> Virtuelles Klassenzimmer mittels KlassRaum Live (ortsunabhängig)</p>
        <p class="body-text schedule-line"><b>Kursdauer:</b> 24 Wochen</p>
        <p class="body-text" style="margin-top:3px"><b>Unterrichtszeiten:</b> Montag bis Freitag von 8:00 – 16:00 Uhr</p>
        <p class="body-text" style="margin-top:3px"><b>Kursstart:</b> Maximale Flexibilität! Aufgrund des rollierenden Systems ist ein Kursstart zu Beginn der jeweiligen Module jederzeit modulunabhängig möglich.</p>
      </section>
    </div>
    <div class="vertical-title">Zielsetzung</div>
    <div class="footer-bar"></div>
  </div>

  <div class="panel panel--navy facts">
    <div class="content">
      <section>
        <svg class="icon" style="left:0;top:12px" width="26" height="32" viewBox="0 0 26 32" fill="none" stroke="#8a93ae" stroke-width="1.4">
          <rect x="2" y="2" width="22" height="28" rx="3"/><rect x="6" y="6" width="14" height="6"/><path d="M6 16h3v3H6zM11.5 16h3v3h-3zM17 16h3v3h-3zM6 22h3v3H6zM11.5 22h3v3h-3zM17 22h3v3h-3z"/>
        </svg>
        <h2 class="heading" style="margin-left:32px">Kosten</h2>
        <p class="body-text" style="margin-left:32px">Die Maßnahme ist nach AZAV durch die ZertPro als fachkundige Stelle zugelassen und erfüllt damit die Voraussetzung der Förderung über einen Bildungsgutschein</p>
        <p class="body-text">durch die Agentur für Arbeit (SGB III) bzw. JobCenter (SGB II), durch Rentenversicherungsträger oder nach dem Soldatenversorgungsgesetz von bis 100 % der Kosten. Die lokalen Agenturen für Arbeit bzw. JobCenter, die Rentenversicherungsträger oder die Berufsförderungsdienste erteilen hierzu nähere Auskünfte.</p>
      </section>
      <section>
        <h2 class="heading">Inhalte</h2>
        <p class="subhead">Wirtschaftsbezogene Qualifikationen</p>
        <ul class="list">
          <li>Volks- und Betriebswirtschaft</li><li>Rechnungswesen</li><li>Recht und Steuern</li><li>Unternehmensführung</li>
        </ul>
        <p class="subhead">Handlungsspezifische Qualifikationen</p>
        <ul class="list">
          <li>Betriebliches Management</li><li>Investition, Finanzierung, betriebliches Rechnungswesen und Controlling</li><li>Logistik</li><li>Marketing und Vertrieb</li><li>Führung und Zusammenarbeit</li>
        </ul>
      </section>
      <section>
        <svg class="icon" style="left:146px;top:-4px" width="36" height="28" viewBox="0 0 38 30" fill="none" stroke="#8a93ae" stroke-width="1.4">
          <path d="M2 5c6-2 11-1 16 2v20c-5-3-10-4-16-2zM36 5c-6-2-11-1-18 2v20c7-3 12-4 18-2z"/>
        </svg>
        <h2 class="heading" style="width:130px">Ihr persönlicher Vorteil</h2>
        <ul class="list">
          <li>Zeugnis des Trägers und/oder Teilnahmebescheinigung</li><li>Bundesweit anerkannter IHK-Abschluss</li><li>Querschnittsübergreifendes Fachwissen</li><li>Qualifizierung zur Übernahme einer höheren Position</li>
        </ul>
        <p class="body-text" style="margin-top:8px;font-size:6.6px">Weiterqualifizierung zum Master Professional of Business Management (CCI) ist nach Erhalt des Abschlusses möglich</p>
      </section>
    </div>
  </div>

  <div class="panel cover">
    <div class="cover-photo" role="img" aria-label="Foto: junge Frau im hellen Kleid läuft mit ausgebreiteten Armen durch ein Getreidefeld unter hellem Himmel"></div>
    <div class="brand-tab"><span class="brand-dot"></span></div>
    <div class="cover-title">
      <div class="brand-name">Lernhöhe</div>
      <h1>Aufstiegsfortbildung</h1>
    </div>
    <div class="cover-band">Werde jetzt <b>Geprüfte/r<br>Wirtschaftsfachwirt/in</b> (IHK)</div>
  </div>
</div>

<div class="sheet sheet--inside">

  <div class="panel panel--navy career">
    <div class="brand-line"><span class="brand-dot"></span><span class="brand-name">Lernhöhe</span></div>
    <div class="content">
      <p class="body-text">Eine <b>Aufstiegsfortbildung zum/zur Wirtschaftsfachwirt/-in</b> vermittelt generalistisches Fachwissen im Bereich Handel, Industrie sowie Dienstleistungen und zählt insofern als Aufstiegsfortbildung zu den populärsten Aufstiegsfortbildungen im kaufmännischen Bereich. Wirtschaftsfachwirte übernehmen in der Regel Führungsaufgaben und können betriebswirtschaftliche Zusammenhänge in ihrem Gesamtzusammenhang erkennen und beurteilen.</p>
      <p class="body-text">Der Abschluss zum/zur Wirtschaftsfachwirt/-in ist eine echte Alternative zum klassischen Bachelorstudium an einer Hochschule. Der wesentliche Unterschied liegt in der praxisnahen Auslegung der Theorieinhalte.</p>
      <p class="body-text" style="font-size:7.2px">Mit der Zuordnung auf DQR-Stufe 6 befindet sich der Abschluss auf derselben Stufe wie die Bachelor-Abschlüsse der Hochschulen.</p>
      <svg width="40" height="44" viewBox="0 0 40 44" fill="none" stroke="#8a93ae" stroke-width="1.5" style="margin-left:90px">
        <rect x="4" y="3" width="26" height="32" rx="2"/><path d="M9 10h16M9 15h16M9 20h12"/><circle cx="28" cy="31" r="6"/><path d="M25 36l-2 7 5-3 5 3-2-7"/>
      </svg>
    </div>
    <div class="vertical-title">Aufstiegsfortbildung</div>
  </div>

  <div class="panel panel--light entry">
    <div class="brand-tab"><span class="brand-dot"></span><span class="brand-name">Lernhöhe</span></div>
    <div class="content">
      <h2 class="heading">Fachliche Voraussetzungen</h2>
      <p class="body-text">Für die Teilprüfung<br><b>„Wirtschaftsbezogene Qualifikationen“</b></p>
      <ul class="list">
        <li>werden Sie zugelassen, wenn Sie eine erfolgreich bestandene Abschlussprüfung in einem anerkannten mindestens dreijährigen kaufmännischen oder verwaltenden Ausbildungsberuf haben, oder</li>
        <li>eine erfolgreich bestandene Abschlussprüfung in einem sonstigen anerkannten mindestens dreijährigen Ausbildungsberuf und danach mindestens ein Jahr Berufspraxis vorweisen können, oder</li>
        <li>eine erfolgreich bestandene Abschlussprüfung in einem anderen anerkannten Ausbildungsberuf und danach mindestens zwei Jahre Berufspraxis gesammelt haben, oder</li>
        <li>mindestens drei Jahre Berufspraxis vorweisen können.</li>
      </ul>
      <p class="body-text" style="margin-top:5px">Für die Teilprüfung<br><b>„Handlungsspezifische Qualifikationen“</b></p>
      <p class="body-text" style="padding-left:6px">werden Sie zugelassen, wenn die abgelegte Teilprüfung „Wirtschaftsbezogene Qualifikationen“ nicht länger als fünf Jahre zurückliegt und Sie mindestens ein weiteres Jahr Berufspraxis zu den Zulassungsvoraussetzungen unter der Teilprüfung „Wirtschaftsbezogene Qualifikationen“ nachweisen können.</p>
      <p class="note">Den Antrag auf Prüfung der Zulassungsvoraussetzungen erhalten Sie bei Ihrer zuständigen Industrie- und Handelskammer.</p>
    </div>
    <div class="footer-bar"></div>
  </div>

  <div class="panel panel--navy tech">
    <div class="vertical-title">Voraussetzungen</div>
    <div class="brand-line"><span class="brand-dot"></span><span class="brand-name">Lernhöhe</span></div>
    <div class="content">
      <section>
        <h2 class="heading">Technische Voraussetzungen</h2>
        <p class="body-text">Für die Teilnahme an der Fortbildung benötigen Sie einen PC, der die folgenden Hardwareanforderungen für Fenstra-Systeme erfüllt:</p>
        <ul class="list" style="margin-top:2px">
          <li>Computer und Prozessor: Mindestens 1,6 GHz (oder höher), 2-Core-Prozessor</li>
          <li>Arbeitsspeicher: 4,0 GB RAM</li>
          <li>Festplatte: 3,0 GB verfügbarer Speicherplatz</li>
          <li>Anzeige: Bildschirmauflösung 1024x768 Pixel</li>
          <li>Grafikkarte: Grafikhardwarebeschleunigung erfordert GrafiX 9 oder höher, mit GTM 2.0 oder höher für Fenstra 10</li>
          <li>Betriebssystem: Fenstra 8</li>
          <li>Video: USB 2.0-Videokamera (oder interne Kamera)</li>
        </ul>
      </section>
      <section>
        <h2 class="heading">Kursanmeldung</h2>
        <p class="body-text" style="font-size:6.4px">Die Kursanmeldung erfolgt nach einem persönlichen Beratungsgespräch.</p>
        <p class="body-text" style="font-size:6.4px;margin-top:4px">Nehmen Sie hierzu gerne Kontakt mit uns auf. Wir freuen uns schon sehr!</p>
      </section>
    </div>
    <svg class="icon" style="left:52px;bottom:40px" width="42" height="40" viewBox="0 0 42 40" fill="none" stroke="#8a93ae" stroke-width="1.5">
      <path d="M4 4h20v30H4z"/><path d="M8 10h12M8 15h12M8 20h8"/><path d="M20 32l16-18 3 3-16 18-5 1z"/>
    </svg>
    <div class="contact">
      <p>Lernhöhe GmbH<br>Birkenweg 14<br>32049 Talbrück</p>
      <p>+49-(0)5221-4410360<br>kontakt@lernhoehe.de<br>www.lernhoehe.de</p>
    </div>
  </div>
</div>

</body>
</html>
```